EPIC, awesome, creative business card needed - get involved!

I'm launching a boutique, exclusive Property Management real estate agency in Sydney early next year.
The name of the agency will be called "Quartz Hill Lane" - it's a play on "chase the silver pebble trail" to wealth. The Quartz Hill Lane signifies wealth through property investment.
My business will offer management of investment properties (ie Property Management).
The difference with Quartz Hill Lane and other agencies is the business will be run by one of Australia's leading property investment experts, and also one of Australia's leading property managers.
It will be exclusively for high net worth properties and individuals, so the business card needs to be extremely sharp, slick and relatively simple.
The information I want on the card is as follows
Nolan Pryce - Director
M: 0412 967 154
P: 9735 6021
E: nolan@quartzhilllane.net.au
W: quartzhilllane.net.au
I'm happy with the red from the logo, black - no yellows or funky colors. I want this to be a super corporate and slick business card to match the high end nature of the business.
Good luck everyone, and please ask questions for clarification.

```html
<!DOCTYPE html>
<html lang="en">
<head>
<meta charset="utf-8">
<title>Quartz Hill Lane — Business Card</title>
<link rel="stylesheet" href="https://fonts.googleapis.com/css2?family=Saira+Condensed:wght@500;600;700&display=swap">
<style>
  :root {
    --backdrop: #e6e7e8;
    --card: #f3f4f4;
    --card-edge: #d9dcdd;
    --brand-red: #e0392f;
    --reverse: #ffffff;
    --ink: #2b2626;
    --label-grey: #c2bfbd;
  }
  * { margin: 0; padding: 0; box-sizing: border-box; }
  html, body {
    width: 1200px;
    height: 1000px;
    overflow: hidden;
    background: var(--backdrop);
    font-family: "Saira Condensed", "Arial Narrow", sans-serif;
  }
  .stage {
    position: relative;
    width: 1200px;
    height: 1000px;
  }
  .business-card {
    position: absolute;
    left: 180px;
    top: 250px;
    width: 785px;
    height: 500px;
    background: var(--card);
    border: 1px solid var(--card-edge);
    border-radius: 4px;
    box-shadow: 0 16px 36px rgba(0, 0, 0, 0.10);
  }
  .brand-block {
    position: absolute;
    left: 110px;
    top: 105px;
    width: 246px;
    height: 287px;
    background: var(--brand-red);
    display: flex;
    align-items: center;
    padding: 0 20px;
  }
  .brand-name {
    color: var(--reverse);
    font-weight: 700;
    font-size: 28px;
    line-height: 1;
    text-transform: uppercase;
    letter-spacing: 1px;
    white-space: nowrap;
  }
  .person {
    position: absolute;
    left: 465px;
    top: 170px;
  }
  .person-name {
    color: var(--brand-red);
    font-weight: 700;
    font-size: 38px;
    line-height: 1;
    text-transform: uppercase;
    letter-spacing: 1px;
  }
  .person-role {
    color: var(--ink);
    font-weight: 600;
    font-size: 17px;
    line-height: 1;
    text-transform: uppercase;
    letter-spacing: 1px;
    margin-top: 8px;
  }
  .contact-list {
    position: absolute;
    left: 424px;
    top: 270px;
    display: grid;
    grid-template-columns: 16px auto;
    column-gap: 26px;
    row-gap: 1px;
    list-style: none;
  }
  .contact-list::before {
    content: "";
    position: absolute;
    left: 29px;
    top: 2px;
    bottom: -6px;
    width: 2px;
    background: var(--label-grey);
  }
  .contact-item { display: contents; }
  .contact-label {
    color: var(--label-grey);
    font-weight: 500;
    font-size: 18px;
    line-height: 28px;
    text-align: center;
    text-transform: uppercase;
  }
  .contact-value {
    color: var(--ink);
    font-weight: 500;
    font-size: 20px;
    line-height: 28px;
    text-transform: uppercase;
    letter-spacing: 1.5px;
  }
</style>
</head>
<body>
  <main class="stage">
    <article class="business-card">
      <div class="brand-block">
        <span class="brand-name">Quartz Hill Lane</span>
      </div>

      <div class="person">
        <h1 class="person-name">Nolan Pryce</h1>
        <p class="person-role">Director</p>
      </div>

      <ul class="contact-list">
        <li class="contact-item"><span class="contact-label">M</span><span class="contact-value">0412 967 154</span></li>
        <li class="contact-item"><span class="contact-label">P</span><span class="contact-value">9735 6021</span></li>
        <li class="contact-item"><span class="contact-label">E</span><span class="contact-value">nolan@quartzhilllane.net.au</span></li>
        <li class="contact-item"><span class="contact-label">W</span><span class="contact-value">quartzhilllane.net.au</span></li>
      </ul>
    </article>
  </main>
</body>
</html>
```